Flyer Designer for a Widow and Door Company - loooking for fresh design

We are looking for a flyer designed to advertise our business - we supply and install windows and doors - we are looking for a fresh looking flyer to distribute to drum up business - more information can be found at our website www.brightsashdepot.co.uk - We want a different approach than we currently have - making it vibrant and fresh - you can see the services on the website but its more the graphical design that we are looking for rather than content as the content from the website can be used for each service etc.

Target Market(s)

the general public

Colors

Designer to choose colors to be used in the design.

Requirements
Must have
• vibrant design and images

```html
<!DOCTYPE html>
<html lang="en">
<head>
<meta charset="utf-8">
<title>Bright Sash Depot – Flyer</title>
<link rel="stylesheet" href="https://fonts.googleapis.com/css2?family=Montserrat:ital,wght@0,400;0,600;0,700;0,800;1,700;1,800&display=swap">
<style>
  :root{
    --blue:#2f6fc4;
    --blue-dark:#1f4f93;
    --grey:#8a8c90;
    --grey-light:#c9cbce;
    --grey-pale:#e6e7e9;
    --ink:#2a3544;
    --white:#ffffff;
    --backdrop:#d7d8da;
  }
  *{box-sizing:border-box;margin:0;padding:0}
  html,body{width:1200px;height:2400px;overflow:hidden;background:var(--backdrop);font-family:"Montserrat",sans-serif}
  .flyer{position:absolute;left:50px;top:422px;width:1100px;height:1556px;background:var(--white);overflow:hidden;box-shadow:0 10px 40px rgba(0,0,0,.18)}
  .flyer-shapes{position:absolute;inset:0}
  .abs{position:absolute}

  .brand{left:40px;top:44px;display:flex;align-items:center;gap:18px}
  .brand-mark{width:70px;height:70px;background:var(--blue)}
  .brand-name{font-weight:800;font-size:40px;line-height:1;color:var(--blue-dark);letter-spacing:.5px;width:330px}
  .brand-tagline{left:40px;top:140px;font-weight:700;font-size:19px;color:var(--blue);letter-spacing:1.5px}

  .call{right:44px;top:48px;text-align:right;color:var(--white)}
  .call-label{font-weight:800;font-style:italic;font-size:46px}
  .call-number{font-weight:800;font-size:56px;margin-top:6px;letter-spacing:1px}

  .intro{left:40px;top:200px;width:290px;font-size:17px;line-height:1.45;color:var(--ink)}
  .intro p+p{margin-top:16px}
  .intro strong{color:var(--blue-dark)}

  .headline{left:40px;top:862px;font-weight:800;font-size:60px;line-height:72px;color:var(--white);text-transform:uppercase}

  .services-title{left:740px;top:880px;font-weight:700;font-size:56px;line-height:60px;color:var(--white)}
  .services{left:730px;top:1010px;width:340px;list-style:none}
  .service{display:flex;gap:20px;margin-bottom:16px;color:var(--white)}
  .service-icon{flex:0 0 62px;height:62px;border-radius:50%;background:var(--white);display:flex;align-items:center;justify-content:center}
  .service h3{font-size:18px;font-weight:800;letter-spacing:.5px;margin-bottom:4px;line-height:22px}
  .service p{font-size:14px;line-height:19px}

  .gallery{left:40px;top:1296px;display:flex;gap:8px}
  .gallery figure{width:96px}
  .gallery .photo{width:96px;height:126px}
  .gallery figcaption{font-size:14px;font-weight:600;color:var(--ink);margin-top:4px}

  .address{left:40px;top:1480px;width:560px;font-size:14px;color:var(--ink);line-height:1.4}
  .social{right:40px;top:1426px;display:flex;gap:14px}
  .social span{width:46px;height:46px;border-radius:50%;border:3px solid var(--white)}
  .website{right:40px;top:1496px;font-size:17px;font-weight:700;color:var(--white)}
</style>
</head>
<body>
<main class="flyer">
  <svg class="flyer-shapes" viewBox="0 0 1100 1556" width="1100" height="1556">
    <polygon points="700,0 1100,0 1100,290 600,290" fill="var(--blue)"/>
    <rect x="820" y="290" width="280" height="290" fill="#23304a" role="img" aria-label="Photo of a dark composite front door with glazed panel"/>
    <polygon points="700,330 790,420 700,510 610,420" fill="var(--blue)"/>
    <polygon points="1010,540 1080,610 1010,680 940,610" fill="var(--blue)"/>
    <polygon points="870,560 920,610 870,660 820,610" fill="var(--grey-light)"/>
    <polygon points="560,270 800,500 560,740 320,500" fill="#8fa4b8" role="img" aria-label="Photo of a grey rendered house with white windows and a yellow front door"/>
    <polygon points="360,700 420,760 360,820 300,760" fill="var(--grey-light)"/>
    <polygon points="790,700 850,760 790,820 730,760" fill="var(--grey-pale)"/>
    <polygon points="0,810 500,810 720,1040 480,1270 0,1270" fill="var(--grey)"/>
    <polygon points="560,870 610,920 560,970 510,920" fill="var(--grey-light)"/>
    <polygon points="860,790 1100,790 1100,1556 650,1556 650,1010" fill="var(--blue)"/>
    <rect x="0" y="1450" width="600" height="106" fill="var(--white)"/>
  </svg>

  <div class="abs brand">
    <span class="brand-mark"></span>
    <span class="brand-name">BRIGHT SASH DEPOT LTD</span>
  </div>
  <div class="abs brand-tagline">BESPOKE WINDOWS &amp; DOORS</div>

  <div class="abs call">
    <div class="call-label">Call Us Today</div>
    <div class="call-number">01632 960418</div>
  </div>

  <div class="abs intro">
    <p><strong>Bright Sash Depot</strong> are Suppliers and Installers of quality windows and doors across Northamptonshire and surrounding villages.</p>
    <p>Offering a friendly, customer focused approach to your replacement windows and doors. Providing a full colour range of uPVC and aluminium to compliment any home.</p>
  </div>

  <h1 class="abs headline">Installers<br>&amp; Suppliers<br>of Bespoke<br>Windows<br>&amp; Doors</h1>

  <h2 class="abs services-title">Our<br>Services</h2>
  <ul class="abs services">
    <li class="service">
      <span class="service-icon"><svg width="30" height="30" viewBox="0 0 30 30"><rect x="3" y="3" width="24" height="24" fill="none" stroke="var(--blue)" stroke-width="3"/><line x1="15" y1="3" x2="15" y2="27" stroke="var(--blue)" stroke-width="3"/><line x1="3" y1="15" x2="27" y2="15" stroke="var(--blue)" stroke-width="3"/></svg></span>
      <div><h3>UPVC WINDOWS</h3><p>Energy efficient uPVC windows designed to suit your home, fitted by our trained team.</p></div>
    </li>
    <li class="service">
      <span class="service-icon"><svg width="30" height="30" viewBox="0 0 30 30"><rect x="7" y="2" width="16" height="26" fill="none" stroke="var(--blue)" stroke-width="3"/><circle cx="19" cy="16" r="1.8" fill="var(--blue)"/></svg></span>
      <div><h3>UPVC DOORS</h3><p>Secure uPVC doors in a full colour range, built to last and easy to maintain.</p></div>
    </li>
    <li class="service">
      <span class="service-icon"><svg width="30" height="30" viewBox="0 0 30 30"><line x1="5" y1="5" x2="25" y2="25" stroke="var(--blue)" stroke-width="4"/><line x1="25" y1="5" x2="5" y2="25" stroke="var(--blue)" stroke-width="4"/></svg></span>
      <div><h3>REPAIRS</h3><p>Fast repairs for locks, handles, hinges and misted glass units across the local area.</p></div>
    </li>
    <li class="service">
      <span class="service-icon"><svg width="30" height="30" viewBox="0 0 30 30"><polygon points="15,3 28,14 24,14 24,27 6,27 6,14 2,14" fill="var(--blue)"/></svg></span>
      <div><h3>LANDLORD SERVICES</h3><p>Reliable window and door services for landlords, with quick turnaround on every property.</p></div>
    </li>
  </ul>

  <div class="abs gallery">
    <figure><div class="photo" style="background:#5b4636" role="img" aria-label="Before photo of an old front door"></div><figcaption>Before</figcaption></figure>
    <figure><div class="photo" style="background:#2b3850" role="img" aria-label="After photo of a new front door"></div><figcaption>After</figcaption></figure>
    <figure><div class="photo" style="background:#7a7c78" role="img" aria-label="Before photo of an old back door"></div><figcaption>Before</figcaption></figure>
    <figure><div class="photo" style="background:#e8e8e4" role="img" aria-label="After photo of a new white door"></div><figcaption>After</figcaption></figure>
  </div>

  <div class="abs address">Harbour Yard, Mill Lane, Kettlebrook, Northamptonshire NN9 4ZX</div>
  <div class="abs social"><span></span><span></span><span></span></div>
  <div class="abs website">www.brightsashdepot.co.uk</div>
</main>
</body>
</html>
```